New Label Design Project - Quillfen Dermal

Label Design Brief - Quillfen Dermal
Label Panel Dimensions 1.25" W x 2.375" H (front/back panel)
Hello - our company develops novel products for the skin, & hair care industry as well as dietary supplements. We're looking for a label design for a new product. The product is a premium Topical hair loss/growth serum. I attached the brand logo & 2 other sister products along with some competitive products.
The product is a topical natural hair loss serum for men & women to regrow new hair and help restore hair loss & thinning hair due to vitamin deficiencies, hormone imbalance & aging. It is a science based efficacious serum with a century’s old medicinal herbal formula.
Attached is our logo & some files of other competition. The label must have an upscale, technology flair to it. The product is clinically effective, leveraged by Ancient Wisdom and Modern Science.
Below are attached files of 2 of our products & other generic competition for your perusal.

https://www.shopvarlo.example/item/K7R2TQ4MPL?ref=lst_featured

https://www.shopvarlo.example/item/K7R3ZN8WDH/ref=lst-redir?pg=1&ref=lst_lowprice

Target Market(s)

men & women age 18-80

Requirements
Must have
• see brief
Should not have
• Please do not have a picture of a man or a women on the label.

```html
<!DOCTYPE html>
<html lang="en">
<head>
<meta charset="UTF-8">
<title>Quillfen Dermal – Growth Activator DHT Blocker Label</title>
<link href="https://fonts.googleapis.com/css2?family=Montserrat:wght@700;800;900&family=Open+Sans:wght@400;600;700&display=swap" rel="stylesheet">
<style>
  :root {
    --backdrop: #a4683a;
    --label-white: #ffffff;
    --rule-dark: #3a2316;
    --rule-bronze: #9a6a40;
    --band-bronze-dark: #4a2a17;
    --band-bronze-light: #8d5a32;
    --band-espresso: #1d1310;
    --band-espresso-light: #3a2820;
    --headline-silver: #e4e4e4;
    --gold-light: #e8d3a0;
    --gold-dark: #9a7a45;
    --ink: #1e1a18;
    --brand-brown: #8a5a32;
    --bar-black: #050505;
    --placeholder-grey: #d9d9d9;
  }
  * { margin: 0; padding: 0; box-sizing: border-box; }
  html, body { width: 1200px; height: 1200px; overflow: hidden; }
  body {
    background: var(--backdrop);
    font-family: "Open Sans", sans-serif;
    position: relative;
  }
  .label {
    position: absolute;
    left: 320px;
    top: 80px;
    width: 560px;
    height: 1040px;
    background: var(--label-white);
  }
  .rule {
    position: absolute;
    left: 10px;
    right: 10px;
    height: 7px;
    background: linear-gradient(90deg, var(--rule-dark), var(--rule-bronze) 60%, var(--rule-dark));
  }
  .rule--top { top: 0; }
  .rule--bottom { top: 1034px; }
  .brand-name {
    position: absolute;
    top: 140px;
    left: 0;
    width: 100%;
    text-align: center;
    font-family: "Open Sans", sans-serif;
    font-weight: 400;
    font-size: 42px;
    letter-spacing: 1px;
    color: var(--brand-brown);
  }
  .band-growth {
    position: absolute;
    top: 243px;
    left: 8px;
    width: 550px;
    height: 158px;
    background: linear-gradient(90deg, var(--band-bronze-dark), var(--band-bronze-light) 55%, var(--band-bronze-dark));
    display: flex;
    flex-direction: column;
    align-items: center;
    justify-content: center;
    font-family: "Montserrat", sans-serif;
    font-weight: 800;
    font-size: 60px;
    line-height: 1.05;
    color: var(--headline-silver);
  }
  .band-dht {
    position: absolute;
    top: 401px;
    left: 0;
    width: 558px;
    height: 246px;
    background: radial-gradient(ellipse at 60% 40%, var(--band-espresso-light), var(--band-espresso) 75%);
    text-align: center;
  }
  .dht-word {
    display: block;
    margin-top: 4px;
    font-family: "Montserrat", sans-serif;
    font-weight: 900;
    font-size: 168px;
    line-height: 1;
    letter-spacing: 4px;
    background: linear-gradient(180deg, var(--gold-light), var(--gold-dark));
    -webkit-background-clip: text;
    background-clip: text;
    color: transparent;
  }
  .blocker-word {
    display: block;
    font-family: "Montserrat", sans-serif;
    font-weight: 800;
    font-size: 62px;
    line-height: 1;
    color: var(--headline-silver);
  }
  .molecule-art {
    position: absolute;
    top: 630px;
    left: 155px;
    width: 235px;
    height: 195px;
    border-radius: 40%;
    background: radial-gradient(ellipse, #9a9a9a, #dcdcdc 70%, transparent 72%);
  }
  .audience-bar {
    position: absolute;
    top: 838px;
    left: 0;
    width: 553px;
    height: 50px;
    background: var(--bar-black);
    color: #ffffff;
    font-size: 25px;
    letter-spacing: 2px;
    display: flex;
    align-items: center;
    justify-content: center;
  }
  .claims {
    position: absolute;
    top: 902px;
    left: 64px;
    list-style: none;
    font-family: "Open Sans", sans-serif;
    font-weight: 700;
    font-size: 19px;
    color: var(--ink);
    line-height: 32px;
  }
  .claims li { display: flex; align-items: center; gap: 6px; }
  .claims svg { width: 12px; height: 12px; }
  .mortar-art {
    position: absolute;
    top: 890px;
    left: 338px;
    width: 118px;
    height: 116px;
    background: radial-gradient(ellipse at 50% 60%, #bdbdbd, #ececec 70%, transparent 72%);
  }
  .volume-tab {
    position: absolute;
    top: 972px;
    left: 222px;
    width: 84px;
    height: 52px;
    background: linear-gradient(180deg, var(--band-bronze-light), var(--band-bronze-dark));
    color: #ffffff;
    font-weight: 700;
    font-size: 22px;
    display: flex;
    align-items: center;
    justify-content: center;
  }
</style>
</head>
<body>
  <main class="label">
    <div class="rule rule--top"></div>

    <div class="brand-name">Quillfen Dermal</div>

    <div class="band-growth">
      <span>GROWTH</span>
      <span>ACTIVATOR</span>
    </div>

    <div class="band-dht">
      <span class="dht-word">DHT</span>
      <span class="blocker-word">BLOCKER</span>
    </div>

    <div class="molecule-art" role="img" aria-label="Ball-and-stick model of a steroid molecule"></div>

    <div class="audience-bar">FOR MEN AND WOMEN</div>

    <ul class="claims">
      <li>
        <svg viewBox="0 0 12 12" aria-hidden="true"><circle cx="6" cy="6" r="5" fill="none" stroke="#1e1a18" stroke-width="1.4"/><path d="M3.5 6.2 L5.3 7.9 L8.6 4.3" fill="none" stroke="#1e1a18" stroke-width="1.4"/></svg>
        PARABEN FREE
      </li>
      <li>
        <svg viewBox="0 0 12 12" aria-hidden="true"><circle cx="6" cy="6" r="5" fill="none" stroke="#1e1a18" stroke-width="1.4"/><path d="M3.5 6.2 L5.3 7.9 L8.6 4.3" fill="none" stroke="#1e1a18" stroke-width="1.4"/></svg>
        TIME -RELEASED
      </li>
    </ul>

    <div class="mortar-art" role="img" aria-label="Sketch of a mortar and pestle"></div>

    <div class="volume-tab">2fl.oz</div>

    <div class="rule rule--bottom"></div>
  </main>
</body>
</html>
```